Brackwell + Tasse Architect Marketing campaign for a morern fresh architecture cutting egde firm th...

To create en exciting template for our monthly newsletters to go out to all our clients via email. I have added a bit of an idea of what we like but not limited to..... we like a nice clean fresh look with lots of white space. I hve aslo added a sketch of the type of how we might layt it out - you may have a better idea. also the pics of the projects for the first issue (issue #1)We like the opening page like the attached lumacafe had and replace the cup with apic of our building/office. Cant wait to see what you come up with.

Target Market(s)

young professionals

Industry/Entity Type

Architectural

Font styles to use
Serif

Colors

Designer to choose colors to be used in the design.

Requirements
Must have
• Logo, text information provided, photos provided
Nice to have
• lots of white space, clean and frest looking

```html
<!DOCTYPE html>
<html lang="en">
<head>
<meta charset="utf-8">
<title>Brackwell + Tasse Newsletter – Issue #1</title>
<link href="https://fonts.googleapis.com/css2?family=Lato:wght@400;700&family=Open+Sans:ital,wght@0,400;0,600;0,700;1,400;1,600&family=Raleway:wght@400;500&display=swap" rel="stylesheet">
<style>
:root{
  --backdrop:#000000;
  --paper:#ffffff;
  --ink:#1e1e1e;
  --ink-soft:#3a3a3a;
  --muted:#9a9a9a;
  --muted-light:#b8b8b8;
  --rule:#e6e6e6;
  --panel:#222222;
  --panel-text:#f2f2f2;
  --footer-bar:#dcdcdc;
}
*{margin:0;padding:0;box-sizing:border-box}
html,body{width:1200px;height:2250px;overflow:hidden;background:var(--backdrop)}
body{position:relative;font-family:"Open Sans",Arial,sans-serif;color:var(--ink)}
.newsletter{position:absolute;left:285px;top:52px;width:640px;height:2150px;background:var(--paper);overflow:hidden}
.abs{position:absolute}

/* header */
.masthead{left:0;top:0;width:640px;height:137px;display:flex;align-items:center;justify-content:center;gap:12px}
.masthead .mark{width:22px;height:22px;border:3px solid var(--ink)}
.masthead .brand{font-family:"Lato",sans-serif;font-weight:700;font-size:22px;letter-spacing:2px;color:var(--ink);text-transform:uppercase}

/* hero */
.hero{left:0;top:137px;width:640px;height:363px;
  background:linear-gradient(105deg,#3e3e3c 0%,#4a4a47 50%,#6d6f68 58%,#8a8e86 75%,#9fa596 100%)}
.hero-copy{left:33px;top:50px;width:280px;color:#fff}
.hero-title{font-family:"Lato",sans-serif;font-weight:700;font-size:40px;line-height:50px;letter-spacing:.5px}
.hero-text{font-family:"Lato",sans-serif;font-size:14px;line-height:22.5px;margin-top:18px;width:265px}

/* welcome */
.welcome-title{left:0;top:548px;width:640px;text-align:center;font-family:"Lato",sans-serif;font-size:25px;letter-spacing:1px;color:var(--ink)}
.welcome-rule{left:200px;top:588px;width:240px;height:2px;background:var(--ink)}
.welcome-rule span{position:absolute;left:90px;width:60px;height:2px;background:var(--muted-light)}
.welcome-text{left:60px;top:625px;width:520px;text-align:center;font-size:10.5px;line-height:20px;color:var(--muted-light)}
.issue{left:0;top:746px;width:640px;text-align:center;font-family:"Lato",sans-serif;font-weight:700;font-size:25px;color:var(--muted)}
.divider{left:0;width:640px;height:1px;background:var(--rule)}

/* shared section type */
.sec-title{font-family:"Open Sans",sans-serif;font-weight:600;font-size:19px;letter-spacing:.5px;color:var(--ink);text-transform:uppercase;white-space:nowrap}
.sec-rule{height:2px;background:var(--ink)}
.sec-sub{font-family:"Raleway",sans-serif;font-size:14px;letter-spacing:.6px;color:var(--ink-soft);text-transform:uppercase;white-space:nowrap}
.photo{display:block}
.plus{position:absolute;right:8px;bottom:4px;color:#fff;font-family:"Lato",sans-serif;font-size:24px;line-height:1}
.copy-box{font-size:8.4px;line-height:13.2px;color:var(--panel-text);background:rgba(30,30,30,.92);padding:8px 10px}

/* drawing board */
.db-img-main{left:80px;top:887px;width:281px;height:186px;background:linear-gradient(160deg,#2f2f2f 0%,#4a4a46 45%,#6c7565 70%,#8b8f83 100%)}
.db-img-main .copy-box{position:absolute;left:6px;top:6px;width:180px;background:rgba(25,25,25,.9)}
.db-img-a{left:378px;top:821px;width:183px;height:119px;background:linear-gradient(170deg,#d9dde0 0%,#bfc5c6 40%,#7e8a76 75%,#55604d 100%)}
.db-img-b{left:378px;top:955px;width:183px;height:118px;background:linear-gradient(170deg,#e4e6e8 0%,#9a9c9b 45%,#5a5d58 65%,#6c8651 100%)}

/* under construction */
.uc-img-a{left:80px;top:1105px;width:182px;height:142px;background:linear-gradient(180deg,#9aa4b4 0%,#b7bcc6 45%,#4b4a45 70%,#a59a86 100%)}
.uc-img-b{left:80px;top:1266px;width:182px;height:140px;background:linear-gradient(180deg,#8e95a8 0%,#b5b8c2 45%,#6c6e72 70%,#55524c 100%)}
.uc-box{left:277px;top:1200px;width:284px;height:206px;background:linear-gradient(180deg,#2b2b2b 0%,#2b2b2b 58%,#4a4a48 78%,#6a6660 100%)}
.uc-box .copy-box{background:transparent;text-align:justify;padding:10px 12px}

/* feature */
.ft-panel{left:80px;top:1435px;width:117px;height:280px;background:var(--panel);color:#fff;padding:58px 10px 0 12px}
.ft-panel h3{font-family:"Open Sans",sans-serif;font-weight:700;font-size:17px;line-height:24px;text-transform:uppercase}
.ft-panel p{font-size:12.5px;line-height:19px;text-transform:uppercase;margin-top:4px}
.ft-img-a{left:200px;top:1435px;width:148px;height:143px;background:linear-gradient(180deg,#c9ccd0 0%,#a66a44 45%,#5e5b57 80%,#8b8880 100%)}
.ft-img-b{left:200px;top:1580px;width:148px;height:135px;background:linear-gradient(180deg,#d3d6d9 0%,#7a5a45 40%,#3f3f3f 65%,#9b9a96 100%)}
.ft-box{left:357px;top:1435px;width:204px;height:280px;background:linear-gradient(180deg,#333 0%,#333 68%,#5b5853 85%,#8a8378 100%)}
.ft-box .copy-box{background:transparent;text-align:center;padding:8px 10px}

/* stay connected */
.connect{left:0;top:1762px;width:640px;height:218px;background:var(--panel);color:#fff;text-align:center}
.connect h2{font-family:"Open Sans",sans-serif;font-weight:700;font-size:22px;letter-spacing:2px;margin-top:30px}
.connect p{font-style:italic;font-weight:600;font-size:13px;line-height:22px;margin-top:12px}
.socials{display:flex;justify-content:center;gap:22px;margin-top:26px;font-family:"Open Sans",sans-serif;font-weight:600;font-size:13px;color:#fff}

/* membership */
.membership{left:0;top:1980px;width:640px;height:140px;text-align:center}
.membership h4{font-family:"Open Sans",sans-serif;font-weight:400;font-size:17px;color:var(--ink-soft);margin-top:18px}
.badges{display:flex;justify-content:center;gap:28px;margin-top:16px}
.badge{width:92px;height:52px;background:#d5d5d5}
.badge.alt{background:#1f3f78}
.copyright{left:0;top:2120px;width:640px;height:30px;background:var(--footer-bar);text-align:center;font-size:9px;line-height:30px;color:var(--ink-soft)}
</style>
</head>
<body>
<main class="newsletter">

  <header class="masthead abs">
    <span class="mark"></span>
    <span class="brand">Brackwell + Tasse</span>
  </header>

  <section class="hero abs" role="img" aria-label="Photo of a dark-clad modern house with timber steps and native planting, split by a diagonal light band">
    <svg class="abs" style="left:0;top:0" width="640" height="363" aria-hidden="true">
      <polygon points="330,363 395,0 400,0 335,363" fill="rgba(255,255,255,.35)"/>
    </svg>
    <div class="hero-copy abs">
      <h1 class="hero-title">WE’RE GLAD<br>YOU’RE HERE</h1>
      <p class="hero-text">Now that you are a Brackwell + Tasse Architecture insider you’ll be among the first to hear about upcoming projects that the studio is working on, completed projects, news and more.</p>
    </div>
  </section>

  <h2 class="welcome-title abs">WELCOME TO BRACKWELL + TASSE</h2>
  <div class="welcome-rule abs"><span></span></div>
  <p class="welcome-text abs">It appears that there are a lot of people are genuinely interested in the building and construction industry,and we here at Brackwell + Tasse Architecture often get asked “what we are up to”and “what cool projects have we got on the go”. With that being said we thought we wouldshare with you some of our projects at various stages for you all to enjoy</p>
  <p class="issue abs">Welcome to issue #1</p>
  <div class="divider abs" style="top:800px"></div>

  <!-- On the drawing board -->
  <h3 class="sec-title abs" style="left:80px;top:816px">On the drawing board</h3>
  <div class="sec-rule abs" style="left:80px;top:849px;width:112px"></div>
  <p class="sec-sub abs" style="left:80px;top:857px">Lake Merrin House// Residential</p>
  <div class="db-img-main abs" role="img" aria-label="Rendering of the Lake Merrin two storey house with timber steps">
    <p class="copy-box">We have recently completed this two story house concept overlooking the canals at Lake Merrin here in Kelsbury. We are currently in the Working Drawing phase at present. This house will stand tout from the crowd and has a mixture of cedar, standing seam wall cladding and precast concrete panels. We are really excited to see this project toprogress to construction. We will keep you posted on this one!!</p>
    <span class="plus">+</span>
  </div>
  <div class="db-img-a abs" role="img" aria-label="Rendering of the house beside the canal with trees"><span class="plus">+</span></div>
  <div class="db-img-b abs" role="img" aria-label="Rendering of the house front with lawn"><span class="plus">+</span></div>
  <div class="divider abs" style="top:1090px"></div>

  <!-- Under construction -->
  <div class="uc-img-a abs" role="img" aria-label="Photo of the glazed commercial building at dusk"></div>
  <div class="uc-img-b abs" role="img" aria-label="Photo of the commercial building under evening sky"></div>
  <h3 class="sec-title abs" style="left:335px;top:1116px">Under construction</h3>
  <div class="sec-rule abs" style="left:320px;top:1147px;width:110px"></div>
  <p class="sec-sub abs" style="left:333px;top:1155px;font-size:13.5px">Harlow Street –Stage 1</p>
  <p class="sec-sub abs" style="left:458px;top:1174px;font-size:13.5px">// Commercial</p>
  <div class="uc-box abs" role="img" aria-label="Photo of the construction site with workers and cones">
    <p class="copy-box">This new development currently being construction by Harwood Commercial in Brenton is the anchor development for Harlow Street and the beginning of the reconfiguration / upgrade of the Brenton Town Centre. This is part of a major redevelopment for Brenton. We have worked closely with the Marlow District Council and surrounding residential neighbours so that new development benefits all involved. The building is fully tenanted with Greystone Coffee, Jade Lantern Restaurant, Spice Route Restaurant, Cellar Corner, Thread &amp; Co Clothing Store and a small dairy. Tenants are currently completing fit-outs for the spaces and the project is fast nearing completion and will be open for business in the next few months.</p>
  </div>
  <div class="divider abs" style="top:1420px"></div>

  <!-- Feature project -->
  <div class="ft-panel abs">
    <h3>Feature<br>Project</h3>
    <p>Keystone Cutting &amp; Processing Ltd // Commercial</p>
  </div>
  <div class="ft-img-a abs" role="img" aria-label="Photo of the curved timber-clad office entrance"></div>
  <div class="ft-img-b abs" role="img" aria-label="Photo of the office and factory facade"></div>
  <div class="ft-box abs" role="img" aria-label="Photo of the building during construction with a scissor lift">
    <p class="copy-box">This new office and factory located in the new Kelsbury Business Park is comprised of a large Cutting and Processingfacility for the manufacturer of steel plate profiles. The facility 1,500m² houses two 10-tonne gantry cranes running the full length of the 60 x 25 metre workshopand was designed with the emphasis on maximum plate storage andprofile cutting efficiency. Alongside the processing facility is an attached 238m² modern single level office building has been designed to project the character andbrand of Keystone Cuttingand to sit within the context of the BusinessPark. The interior fit-out uses a limited palette of materials to create a modern uncluttered interior</p>
  </div>

  <!-- Footer -->
  <section class="connect abs">
    <h2>STAY CONNECTION WITH US</h2>
    <p>Also remember to follow us on our social media platforms<br>where are keeping our followers up to date frequently.</p>
    <div class="socials"><span>Lenslog</span><span>Friendwall</span><span>Homefolio</span></div>
  </section>

  <section class="membership abs">
    <h4>Professional Membership</h4>
    <div class="badges"><span class="badge"></span><span class="badge alt"></span></div>
  </section>

  <footer class="copyright abs">Copyright text here</footer>
</main>
</body>
</html>
```